Corporate services company needs a brochure

We are starting a company offering setup services to companies new to that location.
This includes services such as recruitment, company formation, advertising, marketing, pr, handling legal issues, logistics, transportation, procurement,immigration services, corporate gifts, accomodation,entertainment, training, administrative services etc.
Basically taking the setup issues off the hands of the company allowing them focus on their core business.

We are looking to design a professional brochure which would give the potential customers the confidence to entrust us with their needs.

We will be including some copy that can be used but i would very much like for you to bring what i have written to life - adding, deducting and amending where required.

We are looking at a A4 4/6 paged brochure but open to suggestions.

                                       

If you have any images that are suitable, please let us know. We will also be searching for some to add.

The first prize has been increased.

Thanks

Reason: We have just guaranteed the payment and we are hoping that this will encourage good designers to participate.

Reason: Some designers have requested more time to complete their final design.

Hi, I h extended the deadline to give designers more time to work on designs.

we are also looking at making the brochure a height of 8.5 and a width of 11. Please let me know your thoughts on this as any advice will help. The whole objective is to make it look as up to date and creative as possible. There is also another design size of 7.5 by 8.5

Thanks

                                        Hi

The copy has been revised and uploaded.

Hopefully it will give a clearer explanation of what we are trying to do.

Please let me know if you have any further questions.

Thanks

Marta

Reason: adding finishing touches to designs

Reason: We are amending the copy for the brochure

Reason: The new copy for the brochure is ready. I am sorry it has taken so long to get it out. I am sure we will not be making any amendments to it post today. Thanks for your patience The extension is not to attact new designs it is for existing designs's copy to be modified to include information from the updated copy.

Target Market(s)

medium to large companies in banking, telecom, retail etc. It will be viewed by middle and top management.

Industry/Entity Type

Legal

Requirements
Must have
• The brochure must clearly highlight all our services without just listing as this would risk it appearing as if we have just included everything we could think of!,
Please do not do the sitting round the conference table brochure or the typical blue and white brochure.
I desperately need it to be different, unique and serious enough to show that we are capable of handling/managing all what we have included.
Our clients include the many companies starting up an office in Africa.
We are anxious to have the potential clients understand that we will help them setup under any climax/
Nice to have
• modern colours but not too bright. there must still be a clear serious edge to it.
Should not have
• conference room table and people sitting around it.
the typical blue and white brochures often used for these type of services.

```html
<!DOCTYPE html>
<html lang="en">
<head>
<meta charset="utf-8">
<title>Norvale Brochure</title>
<link rel="stylesheet" href="https://fonts.googleapis.com/css2?family=Arimo:wght@400;700&family=Jura:wght@600;700&display=swap">
<style>
:root{
  --green:#3fa844;
  --green-light:#63c45e;
  --green-dark:#1d6a2b;
  --yellow:#f5d800;
  --ink:#222;
  --white:#fff;
  --page:#ffffff;
}
*{box-sizing:border-box;margin:0;padding:0}
html,body{width:1200px;height:900px;overflow:hidden;background:var(--page)}
body{position:relative;font-family:"Arimo",Arial,sans-serif;color:var(--ink)}
.sheet{position:absolute;overflow:hidden;box-shadow:0 3px 8px rgba(0,0,0,.3)}

/* cover */
.cover{left:0;top:15px;width:850px;height:285px;background:var(--green)}
.cover-art{position:absolute;left:0;top:0;width:850px;height:285px}
.brand{position:absolute;left:150px;top:160px;color:var(--white);font-size:17px;font-weight:700;letter-spacing:1px}
.brand-dot{display:inline-block;width:12px;height:12px;border-radius:50%;background:var(--white);margin-right:8px;vertical-align:-1px}
.cover-contact{position:absolute;left:148px;top:220px;color:var(--white);font-size:15px;font-weight:700;line-height:28px}
.cover-tag{position:absolute;font-size:19px;color:#111}
.tag-top{left:518px;top:50px}
.tag-bottom{left:650px;top:205px}
.cover-brand{position:absolute;left:785px;top:258px;font-size:12px;font-weight:700;color:#333;letter-spacing:1px}
.photo{position:absolute;border-radius:50%;border:4px solid var(--white);box-shadow:0 0 0 1px #999}
.photo.ring{border-color:var(--yellow);border-width:5px;box-shadow:none}

/* spreads */
.spread{display:flex}
.inside{left:340px;top:310px;width:855px;height:290px}
.back{left:70px;top:608px;width:835px;height:282px}
.panel{position:relative;flex:1;overflow:hidden;font-size:9px;line-height:1.25;padding:40px 12px 8px}
.panel.light{background:var(--white);color:#111}
.panel.dark{background:var(--green-dark);color:var(--white)}
.panel.light::before{content:"";position:absolute;left:0;top:0;right:0;height:26px;background:linear-gradient(90deg,var(--green),var(--green-light))}
.panel.open{padding-top:12px}
.panel.open::before{display:none}
.panel-title{position:absolute;top:5px;left:0;right:0;text-align:center;font-family:"Jura",Arial,sans-serif;font-weight:700;font-size:15px;color:#111;z-index:1}
.panel.dark .panel-title{color:var(--white)}
.cap{display:inline-block;width:28px;height:28px;line-height:28px;border-radius:50%;background:var(--yellow);color:#111;text-align:center;margin-right:-6px;font-size:18px}
.panel p{margin-bottom:7px;text-align:justify}
.sub{font-family:"Jura",Arial,sans-serif;font-weight:700;font-size:11px;margin:5px 0 4px}
.light .sub{color:var(--green)}
.dark .sub{color:var(--yellow)}
.list{list-style:disc;padding-left:20px;font-size:7px;line-height:1.5;margin-bottom:7px}
</style>
</head>
<body>

<section class="sheet cover">
  <svg class="cover-art" viewBox="0 0 850 285" aria-hidden="true">
    <defs>
      <linearGradient id="wave" x1="0" y1="0" x2="1" y2="0">
        <stop offset="0" stop-color="#e6e6e6"/><stop offset="1" stop-color="#ffffff"/>
      </linearGradient>
    </defs>
    <path d="M430 0 H850 V285 H520 C410 285 400 220 430 150 C460 80 380 40 430 0 Z" fill="url(#wave)"/>
  </svg>
  <div class="brand"><span class="brand-dot"></span>Norvale</div>
  <div class="cover-contact">www.norvale-demo.com<br>1 800 555 0199</div>
  <div class="cover-tag tag-top">excellence...</div>
  <div class="cover-tag tag-bottom">in everything we do</div>
  <div class="cover-brand">Norvale</div>
  <div class="photo" role="img" aria-label="Blue digital network illustration" style="left:470px;top:105px;width:80px;height:80px;background:radial-gradient(#4fb3ff,#0b2c6b)"></div>
  <div class="photo" role="img" aria-label="Cluster of green cubes with one red cube" style="left:555px;top:70px;width:120px;height:130px;border:none;box-shadow:none;border-radius:8px;background:linear-gradient(135deg,#7be07a,#2f9a35)"></div>
  <div class="photo" role="img" aria-label="Business charts and data screen" style="left:710px;top:45px;width:82px;height:82px;background:radial-gradient(#9fd4e8,#1f5a78)"></div>
  <div class="photo" role="img" aria-label="Businessman in a server room" style="left:487px;top:205px;width:80px;height:80px;background:linear-gradient(#8aa0b8,#3b4a5c)"></div>
  <div class="photo" role="img" aria-label="Businessman on the phone" style="left:637px;top:240px;width:70px;height:70px;background:linear-gradient(#d9d9d9,#555)"></div>
</section>

<section class="sheet spread inside">
  <article class="panel light">
    <h2 class="panel-title"><span class="cap">W</span>ho We Are</h2>
    <p>We are an experienced group of professionals committed to providing excellence and inspiring confidence in everything we do while meeting the changing needs of our clients.</p>
    <p>By harnessing the expertise of our carefully chosen advisors, we are able to be the best in-class consultants in all that we do. This success inspires confidence from our clients.</p>
    <h3 class="sub">We do adhere to 3 fundamental values:</h3>
    <ul class="list" style="padding-right:40px">
      <li>Being imaginative in everything we do</li>
      <li>Being purposeful in everything we do</li>
      <li>Being dependable in everything we do</li>
    </ul>
    <p style="padding-right:52px">That is why our message for clients, staff and partners is clear and safe.</p>
  </article>
  <article class="panel dark">
    <h2 class="panel-title"><span class="cap">W</span>hat We Do</h2>
    <h3 class="sub">Virtual Office Package</h3>
    <p>Mail handling, answering phone calls in your company name, the use of a local business address in a prestige location.</p>
    <h3 class="sub">Concierge</h3>
    <p>What your concierge can help with: Entertainment, travel, house comforts, personal shopping, relaxation, cars and transportation, personal and business storage, corporate gifts.</p>
    <p style="padding-left:50px">Norvale is a full-service business development group and general management consultancy firm focused on small and medium sized privately held companies in Africa.</p>
  </article>
  <article class="panel dark">
    <h2 class="panel-title"><span class="cap">O</span>ur Mission</h2>
    <p>Attract reward and retain staffs, who share the company's conviction to be the best at whatever we do.</p>
    <h3 class="sub">Business Setup/Management Services in Africa</h3>
    <p style="padding-right:62px">Need help with planning, raising finance or writing your business plan? We provide information on starting a new business a, a home-based business or buying a business or franchise. We also provide information on exiting a business. Find out about succession plans, bankruptcy.</p>
    <h3 class="sub">Business services</h3>
    <ul class="list"><li>Logos</li><li>Brochures</li><li>Letterhead</li><li>Signage</li></ul>
  </article>
  <article class="panel light">
    <h2 class="panel-title"><span class="cap">W</span>ho Hires Us</h2>
    <p>If you are looking to setup a business or rent an office in Lagos, Norvale offers the services you need.</p>
    <ul class="list">
      <li>Assisting with business incorporation.</li>
      <li>Locating and providing Lagos office suites</li>
      <li>Identifying and vetting appropriate local partners</li>
      <li>Organizing work permits</li>
      <li>Advising on suitable corporate structures.</li>
      <li>Assisting with Relocation (shipping, culture training, domestic staff)</li>
    </ul>
    <p style="padding-left:24px">Norvale provides all the front and back office support your business needs to thrive in Lagos. Finding, quoting and comparing the services your company needs takes time and can slow you down. Let us do it for you!!!!</p>
  </article>
  <div class="photo ring" role="img" aria-label="Businessman in a suit" style="left:172px;top:188px;width:90px;height:90px;background:linear-gradient(#9aa5b0,#2b2f36)"></div>
  <div class="photo ring" role="img" aria-label="Map of Africa with figures" style="left:578px;top:110px;width:80px;height:80px;background:radial-gradient(#f6c85a,#c98a1e)"></div>
</section>

<section class="sheet spread back">
  <article class="panel light">
    <h2 class="panel-title"><span class="cap">O</span>ther Services</h2>
    <p>Our services and expertise can help you drive your business forward. If you require consultation with other entrepreneurs and also need the services we provide, we will construct a plan that includes both. Our goal is to customize an approach that matches your interests, blends in the advice of</p>
    <h3 class="sub">Startup Services</h3>
    <ul class="list">
      <li>General Services</li><li>Business plan (Review and writing)</li><li>Web development</li><li>Logo design</li><li>Network/IT setup and maintenance</li><li>Phone systems</li><li>Office building Advertising</li><li>Cabling</li><li>Accounts/Bookkeeping/Payroll</li><li>Legal</li>
    </ul>
  </article>
  <article class="panel dark open">
    <h3 class="sub">Office Setup</h3>
    <p>We offer expertise through the full lifecycle from concept feasibility and design services to contract preparation, site management, implementation and commissioning. We also cater for the design, procurement and management of public and private assets. These include:</p>
    <ul class="list"><li>Office design and partition</li><li>Renovation</li></ul>
    <p style="padding-left:45px">We align ourselves with a number of international real-estate brokers and professional services firms who specialize in introducing international corporate clients in Lagos. Though these alliances, we are able to support firms by offering additional benefits to their already long list of initiatives.</p>
  </article>
  <article class="panel dark open">
    <h3 class="sub">Last Minute Catering and Corporate Hospitality?</h3>
    <p>Arranging local restaurants or simply ask us to serve gourmet meals directly in your meeting room.</p>
    <h3 class="sub">Human Resource</h3>
    <ul class="list" style="padding-right:50px">
      <li>HR function set-up</li><li>Employee handbooks and policies</li><li>Employee Performance Management</li><li>HR hotline</li><li>Job description</li><li>Phone screening</li><li>Staff screening (referencing and health)</li><li>Offer letters</li><li>Training</li><li>Job posting</li><li>Recruitment.</li>
    </ul>
    <p>Norvale provides all the front and back office support your business needs</p>
  </article>
  <article class="panel light open">
    <p>Our professionals fulfill critical roles in all stages of development and manage those functions in association with our clients. We manage the tasks and talent necessary for tactical success so you can concentrate on your strategic goals.</p>
    <p style="padding-left:58px">We offer a cost effective way to immediately hire the unique combination of expertise required to manage and help your business surge ahead of the competition. We'll always deliver the smartest and most cost effective business infrastructure solutions required to reach your goals and achieve ongoing success.</p>
    <p>We area 'one-stop' shop for startups – whether you're still in PowerPoint modes or further along in the process of starting your new venture, we No matter the stage of your company,</p>
  </article>
  <div class="photo ring" role="img" aria-label="Red and yellow puzzle pieces" style="left:160px;top:165px;width:88px;height:88px;background:radial-gradient(#ffffff,#f2f2f2)"></div>
  <div class="photo ring" role="img" aria-label="Red and blue cubes" style="left:576px;top:92px;width:90px;height:90px;background:linear-gradient(#e04040,#3a7bd5)"></div>
</section>

</body>
</html>
```